Annual review for The Birchmoor Collective

The Birchmoor Collective is a small public relations agency in London specialising in corporate and public affairs. Most of our work is international and we have a strong connection to South Africa. We would like to prepare a short annual review for 2016. The review will serve as both a review of our activities in 2016, and as a credentials document. Content then will include:
1. An introduction to the business
2. Who we are
3. Projects and clients undertaken in 2016
4. News and views
We imagine it will be used mostly as a pdf but would like it to be suitable for print. We envisage it to be about 8 pages long. The design look and feel should convey a business, while small, of stature. We shall include some of our client logos but we would welcome the use of some photography / imagery to have visual impact (although we don't have very much of our own!). The corporate look and feel is white, grey and black.

Industry/Entity Type

Public Relation

Font styles to use
Sans Serif

Requirements
Must have
• My project must convey a business with flair and gravitas, that punches above its weight.
Nice to have
• Thoughtful use of imagery.

```html
<!DOCTYPE html>
<html lang="en">
<head>
<meta charset="utf-8">
<title>The Birchmoor Collective — Annual Review 2016</title>
<link rel="stylesheet" href="https://fonts.googleapis.com/css2?family=Jost:wght@300;400;500;600&display=swap">
<style>
  :root {
    --backdrop: #2b2b2d;
    --paper-light: #eceef3;
    --paper-mid: #d3d5dd;
    --band-dark: #5f6068;
    --band-mid: #80818b;
    --ink: #2e2f35;
    --ink-soft: #4a4b52;
    --white: #ffffff;
    --photo-light: #c9cacd;
    --photo-dark: #3b3c3f;
  }
  * { box-sizing: border-box; margin: 0; padding: 0; }
  html, body { width: 1200px; height: 789px; overflow: hidden; }
  body {
    background: var(--backdrop);
    font-family: "Jost", sans-serif;
    color: var(--ink);
  }
  .spread {
    position: absolute; left: 80px; top: 27px;
    width: 1040px; height: 735px;
    display: flex;
    box-shadow: 0 10px 30px rgba(0,0,0,.5);
  }
  .page { position: relative; width: 520px; height: 735px; overflow: hidden; }

  /* Back cover */
  .back-cover { background: linear-gradient(160deg, var(--white) 0%, var(--paper-light) 45%, var(--paper-mid) 100%); }
  .facets { position: absolute; inset: 0; }
  .views { position: absolute; left: 44px; top: 52px; width: 432px; }
  .views-title { font-weight: 300; font-size: 21px; letter-spacing: 1px; margin-bottom: 10px; }
  .story-title { font-weight: 300; font-size: 17px; margin: 14px 0 6px; }
  .story p { font-size: 7.2px; line-height: 1.45; color: var(--ink-soft); margin-bottom: 6px; }
  .story-lead p { width: 320px; }
  .press-name {
    font-family: "Jost", sans-serif; font-weight: 500; color: var(--ink);
    position: absolute; white-space: nowrap;
  }
  .press-university {
    right: 40px; top: 50px; width: 104px;
    display: flex; align-items: center; gap: 8px;
    font-size: 8px; letter-spacing: 1px; text-transform: uppercase; line-height: 1.3;
    white-space: normal;
  }
  .press-university .mark { width: 24px; height: 24px; background: var(--band-mid); flex: none; }
  .press-university .label { display: block; width: 72px; }
  .press-meridian { right: 60px; top: 268px; font-size: 19px; letter-spacing: 1.5px; text-transform: uppercase; }
  .press-harbour { right: 70px; top: 430px; font-size: 20px; }

  .back-band { position: absolute; left: 0; bottom: 0; width: 520px; height: 230px; }
  .contacts { position: absolute; left: 58px; bottom: 60px; width: 420px; display: flex; gap: 52px; color: var(--white); font-size: 12px; font-weight: 300; }
  .contact-col { display: flex; flex-direction: column; gap: 18px; }
  .contact-item { display: flex; gap: 8px; align-items: flex-start; line-height: 1.3; }
  .contact-item svg { flex: none; margin-top: 2px; }

  /* Front cover */
  .front-cover { background: linear-gradient(180deg, var(--white) 0%, var(--paper-light) 100%); }
  .brand { position: absolute; left: 108px; top: 38px; display: flex; align-items: center; gap: 10px; font-weight: 600; font-size: 21px; color: var(--ink); }
  .brand .dot { width: 22px; height: 22px; border-radius: 50%; border: 2px solid var(--ink); }
  .cover-photo {
    position: absolute; left: 0; top: 94px; width: 520px; height: 470px;
    background: linear-gradient(175deg, var(--photo-light) 0%, #9c9da1 35%, #6c6d71 60%, var(--photo-dark) 100%);
  }
  .front-band { position: absolute; left: 0; bottom: 0; width: 520px; height: 270px; }
  .welcome { position: absolute; right: 40px; bottom: 130px; font-size: 30px; font-weight: 300; letter-spacing: 2px; color: var(--white); }
  .front-web { position: absolute; right: 40px; bottom: 96px; display: flex; gap: 7px; align-items: center; color: var(--white); font-size: 12px; font-weight: 300; }
  .fold { position: absolute; left: 0; top: 0; width: 14px; height: 100%; background: linear-gradient(90deg, rgba(0,0,0,.18), rgba(0,0,0,0)); }
</style>
</head>
<body>
<main class="spread">

  <section class="page back-cover">
    <svg class="facets" width="520" height="735" viewBox="0 0 520 735" aria-hidden="true">
      <polygon points="0,470 520,300 520,520 0,560" fill="#ffffff" opacity=".25"/>
      <polygon points="0,600 300,470 520,520 520,560" fill="#c4c6cf" opacity=".5"/>
    </svg>

    <div class="views">
      <h2 class="views-title">OUR VIEWS</h2>
      <article class="story story-lead">
        <h3 class="story-title">Kestrel Vale and Birchmoor</h3>
        <p>The Birchmoor Collective is pleased to announce it has been retained by Kestrel Vale University, one of South Africa's leading universities, to work on a stakeholder engagement project.</p>
        <p>Founded in 1864, Kestrel Vale routinely ranks among the country's top three universities, with particular strength in science, engineering and law. The appointment builds on our higher education portfolio; in 2015 we were hired by Ashford College, London.</p>
      </article>
      <article class="story">
        <h3 class="story-title">Water corruption</h3>
        <p>Water corruption leaves millions mired in misery: that's the message from our Rowan Ellery in an article published today in The Daily Meridian. Rowan, currently seconded to the Global Water Forum in Paris, used the anti-corruption summit hosted by Prime Minister Helen Marsh to draw attention to the sector's susceptibility to graft.</p>
        <p style="margin-top:34px">Explaining how water cuts across a range of portfolios and disciplines, he writes that this leads to different political and governmental agencies having overlapping and, at times, conflicting responsibilities. To read the article in full, click here.</p>
      </article>
      <article class="story" style="margin-top:26px">
        <h3 class="story-title">Focus on Fukushima</h3>
        <p style="width:250px">Writing in The Harbour Times, our Rowan Ellery highlights the dilemma of water in this most complex post-disaster situation.</p>
        <p style="width:250px">Writing as director of the Global Water Forum, Rowan shows how policymakers face a huge challenge in managing nearly a million tons of contaminated water. To read the letter in full, please click here.</p>
      </article>
    </div>

    <div class="press-name press-university"><span class="mark"></span><span class="label">Kestrel Vale University</span></div>
    <div class="press-name press-meridian">The Daily Meridian</div>
    <div class="press-name press-harbour">The Harbour Times</div>

    <svg class="back-band" viewBox="0 0 520 230" preserveAspectRatio="none" aria-hidden="true">
      <path d="M0,40 Q260,-10 520,30 L520,230 L0,230 Z" fill="var(--band-mid)"/>
      <path d="M0,62 Q260,10 520,52 L520,230 L0,230 Z" fill="var(--band-dark)"/>
    </svg>

    <div class="contacts">
      <div class="contact-col">
        <div class="contact-item">
          <svg width="10" height="13" viewBox="0 0 10 13"><path d="M5 0a4.5 4.5 0 0 0-4.5 4.5C.5 8 5 13 5 13s4.5-5 4.5-8.5A4.5 4.5 0 0 0 5 0zm0 6.3a1.8 1.8 0 1 1 0-3.6 1.8 1.8 0 0 1 0 3.6z" fill="#fff"/></svg>
          <span>42 Fenwick Street<br>London W1K 3RP</span>
        </div>
        <div class="contact-item">
          <svg width="10" height="13" viewBox="0 0 10 13"><path d="M5 0a4.5 4.5 0 0 0-4.5 4.5C.5 8 5 13 5 13s4.5-5 4.5-8.5A4.5 4.5 0 0 0 5 0zm0 6.3a1.8 1.8 0 1 1 0-3.6 1.8 1.8 0 0 1 0 3.6z" fill="#fff"/></svg>
          <span>27, rue des Lilas<br>75011 Paris</span>
        </div>
      </div>
      <div class="contact-col" style="gap:8px">
        <div class="contact-item">
          <svg width="12" height="9" viewBox="0 0 12 9"><rect x=".5" y=".5" width="11" height="8" fill="none" stroke="#fff"/><path d="M.5.5 6 5l5.5-4.5" fill="none" stroke="#fff"/></svg>
          <span>info@birchmoorcollective.com</span>
        </div>
        <div class="contact-item">
          <svg width="11" height="11" viewBox="0 0 11 11"><circle cx="5.5" cy="5.5" r="5" fill="none" stroke="#fff"/><path d="M.5 5.5h10M5.5.5c-2 2.5-2 7.5 0 10M5.5.5c2 2.5 2 7.5 0 10" fill="none" stroke="#fff" stroke-width=".8"/></svg>
          <span>www.birchmoorcollective.com</span>
        </div>
      </div>
    </div>
  </section>

  <section class="page front-cover">
    <div class="brand"><span class="dot"></span><span>The Birchmoor Collective</span></div>
    <div class="cover-photo" role="img" aria-label="Black and white coastal photograph of rocky cliffs and a sea arch above a white-surf bay"></div>
    <svg class="front-band" viewBox="0 0 520 270" preserveAspectRatio="none" aria-hidden="true">
      <path d="M0,110 Q120,40 520,0 L520,270 L0,270 Z" fill="var(--band-mid)"/>
      <path d="M0,140 Q160,60 520,24 L520,270 L0,270 Z" fill="var(--band-dark)"/>
    </svg>
    <div class="welcome">WELCOME</div>
    <div class="front-web">
      <svg width="11" height="11" viewBox="0 0 11 11"><circle cx="5.5" cy="5.5" r="5" fill="none" stroke="#fff"/><path d="M.5 5.5h10M5.5.5c-2 2.5-2 7.5 0 10M5.5.5c2 2.5 2 7.5 0 10" fill="none" stroke="#fff" stroke-width=".8"/></svg>
      <span>www.birchmoorcollective.com</span>
    </div>
    <div class="fold"></div>
  </section>

</main>
</body>
</html>
```